Cobalt Threads and Fuel is looking for a Clothing/Supplement Online Store Website!

Must be convenient, and user friendly, with vibrant colors that catch the eye!

Target Market(s)

Athletes, and Fashion Customers

Industry/Entity Type

Fitness

Coding

Coded - Design and coding required

Number of Pages Required

3 page

Font styles to use
Decorative

Colors

Designer to choose colors to be used in the design.

Requirements
Must have
• Somewhere to feature products, features to promote discounts and make announcements.
Nice to have
• My logos on each page

```html
<!DOCTYPE html>
<html lang="en">
<head>
<meta charset="utf-8">
<title>Cobalt Threads and Fuel — Online Store</title>
<link href="https://fonts.googleapis.com/css2?family=Rajdhani:wght@400;500;600;700&family=Open+Sans:ital,wght@0,400;0,600;1,400&display=swap" rel="stylesheet">
<style>
:root{
  --slate:#587f96;
  --orange:#f26b21;
  --ink:#222;
  --text:#555;
  --muted:#8a8a8a;
  --light:#f2f2f2;
  --panel:#1e1e1e;
  --footer:#1b1b1b;
  --line:#e3e3e3;
  --star:#f5a623;
}
*{box-sizing:border-box;margin:0;padding:0}
html,body{width:1200px;height:4051px;overflow:hidden;background:#fff}
body{position:relative;font-family:"Open Sans",Arial,sans-serif;color:var(--text)}
.abs{position:absolute}
.display{font-family:"Rajdhani","Arial Narrow",sans-serif}
.photo{position:absolute}
.btn{position:absolute;background:var(--orange);color:#fff;font:600 10px/1 "Open Sans",Arial,sans-serif;text-transform:uppercase;display:flex;align-items:center;justify-content:center;letter-spacing:.3px}
.accent{color:var(--orange);font-weight:700}

/* header & hero */
.site-header .logo{left:94px;top:20px;color:#fff;font:700 22px/1 "Rajdhani",sans-serif;letter-spacing:.5px}
.main-nav{left:94px;top:67px;display:flex;gap:0}
.main-nav a{color:#fff;font:500 12px/1 "Rajdhani",sans-serif;text-decoration:none;letter-spacing:.4px;text-transform:uppercase;position:absolute;white-space:nowrap}
.main-nav a.active::after{content:"";position:absolute;left:0;top:17px;width:18px;height:2px;background:#fff}
.util-nav{top:15px;right:94px;display:flex;gap:16px;font-size:10px;color:#999;align-items:center}
.util-nav .login{color:var(--slate);font-weight:600}
.search-btn{left:1078px;top:58px;width:26px;height:26px;border-radius:50%;background:var(--orange)}
.hero-tag{left:778px;top:215px;width:107px;height:21px;border:1px solid #999;font-size:8px;color:#444;display:flex;align-items:center;justify-content:center;text-transform:uppercase}
.hero-title{left:778px;top:256px;font-size:38px;line-height:40px;color:#333;font-weight:400;text-transform:uppercase;letter-spacing:.5px}

/* promos */
.promo-heading{font-family:"Rajdhani",sans-serif;text-transform:uppercase;color:#fff}
.sale-card{left:777px;top:590px;width:329px;height:453px;background:var(--panel);color:#fff;text-align:center}

/* section titles */
.section-title{font:500 34px/1 "Rajdhani",sans-serif;color:#333;text-transform:uppercase;letter-spacing:.5px}

/* product cards */
.product{position:absolute;width:244px}
.product .thumb{position:absolute;left:0;top:0;width:244px;height:272px}
.product.boxed .thumb{border:1px solid var(--line)}
.product .name{position:absolute;left:0;font:500 21px/1 "Rajdhani",sans-serif;color:#333;white-space:nowrap}
.product .name .stars{color:var(--star);font-size:11px;letter-spacing:1px;margin-left:8px;vertical-align:3px}
.product .desc{position:absolute;left:0;width:244px;font-size:13px;line-height:19px;color:#888}
.product .price{position:absolute;left:0;font-size:15px;font-weight:600;color:var(--orange)}
.arrow-btn{position:absolute;width:30px;height:30px;border:1px solid #bbb;border-radius:50%;display:flex;align-items:center;justify-content:center;background:#fff}

/* workout band */
.workout-tag{left:267px;top:1682px;width:106px;height:20px;border:1px solid #999;font-size:8px;color:#444;display:flex;align-items:center;justify-content:center;text-transform:uppercase}
.discount-box{left:209px;top:1816px;width:219px;height:79px;background:#fff;box-shadow:0 3px 14px rgba(0,0,0,.12);text-align:center}

/* about */
.about-title{left:0;width:1200px;top:2698px;text-align:center;font:400 36px/1 "Rajdhani",sans-serif;color:#333;text-transform:uppercase}

/* blog */
.post{position:absolute;width:322px;text-align:center}
.post .thumb{position:absolute;left:0;top:0;width:322px;height:195px}
.post .date{position:absolute;left:24px;top:12px;width:46px;height:46px;border-radius:50%;background:var(--orange);color:#fff;font:italic 600 11px/13px "Open Sans",sans-serif;display:flex;flex-direction:column;align-items:center;justify-content:center}
.post h3{position:absolute;left:0;top:206px;width:322px;font:600 18px/1.2 "Open Sans",sans-serif;color:#333}
.post .meta{position:absolute;left:0;top:244px;width:322px;font:italic 10px/1 "Open Sans",sans-serif;color:#999}
.post .meta b{font-weight:400;color:#555}
.post p{position:absolute;left:0;top:272px;width:322px;font-size:13px;line-height:20px;color:#888}
.post .more{position:absolute;left:0;top:340px;width:322px;font-size:20px;color:#333}

/* footer */
.site-footer{left:0;top:3504px;width:1200px;height:547px;background:var(--footer);color:#aaa}
.f-head{position:absolute;top:56px;font:400 18px/1 "Open Sans",sans-serif;color:#fff}
.f-list{position:absolute;top:96px;list-style:none;font-size:11px;line-height:28px;color:#999}
.f-text{position:absolute;font-size:11px;line-height:17px;color:#999}
.social{position:absolute;top:222px;left:94px;display:flex;gap:6px}
.social span{width:24px;height:24px;border-radius:50%;background:#3b6ea8;display:block}
.social span:nth-child(2){background:#2aa3e0}
.social span:nth-child(3){background:var(--orange)}
.social span:nth-child(4){background:#3f729b}
.contact-row{position:absolute;left:665px;display:flex;gap:10px;font-size:11px;line-height:16px;color:#999}
.contact-row i{flex:none;width:24px;height:24px;border-radius:50%;background:var(--orange);display:flex;align-items:center;justify-content:center}
.nl-input{position:absolute;left:914px;top:165px;width:192px;height:28px;border:1px solid #444;font-size:9px;color:#ccc;padding:9px 10px}
.nl-btn{position:absolute;left:914px;top:200px;width:192px;height:28px;background:var(--orange);color:#fff;font-size:11px;display:flex;align-items:center;justify-content:center;text-transform:uppercase}
.feature{position:absolute;top:314px;display:flex;gap:16px;align-items:center}
.feature i{width:56px;height:56px;border-radius:50%;background:var(--orange);flex:none;display:flex;align-items:center;justify-content:center}
.feature h4{font:600 13px/1 "Open Sans",sans-serif;color:var(--orange);text-transform:uppercase;margin-bottom:3px}
.feature p{font-size:11px;line-height:13px;color:#999;width:200px}
.pay{position:absolute;left:572px;top:430px;display:flex;gap:4px}
.pay span{width:16px;height:10px;border-radius:2px;background:#e53935;display:block}
.pay span:nth-child(2){background:#2c6fd1}
.pay span:nth-child(3){background:#f2b01e}
.pay span:nth-child(4){background:#3aa0e0}
.copyright{position:absolute;left:0;width:1200px;top:476px;text-align:center;font-size:11px;color:#888}
.copyright b{color:#fff;font-weight:400}
</style>
</head>
<body>

<!-- HEADER + HERO -->
<header class="site-header">
  <svg class="abs" style="left:0;top:0" width="1200" height="524" viewBox="0 0 1200 524">
    <rect width="1200" height="524" fill="#587f96"/>
    <polygon points="545,0 1172,0 1106,99 480,99" fill="#fff"/>
    <polygon points="205,499 852,499 828,524 186,524" fill="#fff"/>
  </svg>
  <div class="abs logo">Cobalt Threads and Fuel</div>
  <nav class="abs main-nav">
    <a class="active" style="left:0;top:0">Home</a>
    <a style="left:88px;top:0">Products</a>
    <a style="left:206px;top:0">Blogs</a>
    <a style="left:297px;top:0">Contact Us</a>
  </nav>
  <div class="abs util-nav">
    <span class="login">Login</span>
    <span>My Account ▾</span>
    <span>USD ▾</span>
    <span>🛒 Basket</span>
  </div>
  <div class="abs search-btn">
    <svg width="26" height="26" viewBox="0 0 26 26"><circle cx="12" cy="12" r="4.5" fill="none" stroke="#fff" stroke-width="1.6"/><line x1="15.3" y1="15.3" x2="18" y2="18" stroke="#fff" stroke-width="1.6"/></svg>
  </div>
</header>

<section class="hero">
  <div class="abs" style="left:94px;top:99px;width:1012px;height:400px;background:#f4f4f4"></div>
  <div class="photo" role="img" aria-label="Dark grayscale photo of an athlete stretching" style="left:94px;top:99px;width:384px;height:400px;background:linear-gradient(120deg,#4a4a4a,#1e1e1e 60%,#3a3a3a)"></div>
  <div class="photo" role="img" aria-label="Sprinter in white sportswear in starting position on a running track" style="left:250px;top:118px;width:489px;height:360px;background:linear-gradient(180deg,#e8ece9 0%,#cfd6cf 45%,#6c8a4e 62%,#8b4a3c 78%,#a75a48 100%)"></div>
  <div class="abs hero-tag">Most Popular</div>
  <h1 class="abs display hero-title">The <span class="accent">New Season</span><br>Collection</h1>
  <div class="btn" style="left:782px;top:354px;width:97px;height:30px">Shop Now</div>
</section>

<!-- PROMOS -->
<section class="promos">
  <div class="photo" role="img" aria-label="Man in white compression shirt and black tights" style="left:94px;top:590px;width:328px;height:453px;background:linear-gradient(90deg,#f2f2f2 0%,#ededed 55%,#d9d9d9 75%,#3a3a3a 100%)"></div>
  <div class="abs" style="left:113px;top:751px;font-size:10px;color:#333;text-transform:uppercase">Follow</div>
  <div class="abs display" style="left:113px;top:766px;font-size:27px;color:#333;text-transform:uppercase">Your <span class="accent">Heart</span></div>
  <div class="abs" style="left:113px;top:804px;width:205px;font-size:9px;line-height:14px;color:#666">If you use this site regularly and would like to help keep the site...</div>
  <div class="btn" style="left:115px;top:846px;width:97px;height:30px">Shop Now</div>

  <div class="photo" role="img" aria-label="Group cycling class in a dim gym" style="left:436px;top:590px;width:328px;height:223px;background:linear-gradient(135deg,#3b3835,#1c1a19 60%,#5a4a40)"></div>
  <div class="abs" style="left:436px;top:659px;width:328px;text-align:center;font-size:10px;color:#fff;text-transform:uppercase">Follow</div>
  <div class="abs display promo-heading" style="left:436px;top:672px;width:328px;text-align:center;font-size:27px">Your <span class="accent">Collection</span></div>
  <div class="btn" style="left:551px;top:713px;width:98px;height:28px">Shop Now</div>

  <div class="photo" role="img" aria-label="Woman in sportswear resting on a seaside promenade" style="left:436px;top:821px;width:328px;height:222px;background:linear-gradient(180deg,#8fa2ad 0%,#6d7f8a 45%,#4a555c 100%)"></div>
  <div class="abs" style="left:436px;top:890px;width:328px;text-align:center;font-size:10px;color:#fff;text-transform:uppercase">Collection</div>
  <div class="abs display promo-heading" style="left:436px;top:903px;width:328px;text-align:center;font-size:27px">New <span class="accent">Apparel</span></div>
  <div class="btn" style="left:551px;top:944px;width:98px;height:28px">Shop Now</div>

  <div class="abs sale-card">
    <div class="display" style="position:absolute;left:0;top:55px;width:329px;font-size:28px;font-weight:600;text-transform:uppercase">Summer</div>
    <div class="display" style="position:absolute;left:0;top:85px;width:329px;font-size:96px;line-height:100px;font-weight:700;text-transform:uppercase;letter-spacing:2px">Sale</div>
    <div style="position:absolute;left:22px;top:205px;width:285px;height:1px;background:#555"></div>
    <div style="position:absolute;left:0;top:228px;width:329px;font-size:18px">Get Up To</div>
    <div class="display" style="position:absolute;left:0;top:250px;width:329px;font-size:54px;line-height:60px;font-weight:700;color:var(--orange)">50% <span style="font-weight:400;color:#999;font-size:34px">Off</span></div>
    <div class="btn" style="left:118px;top:333px;width:95px;height:26px">Shop Now</div>
    <div style="position:absolute;left:0;top:375px;width:329px;font-size:10px;color:#ccc">Free Shipping On orders Over $99</div>
  </div>
</section>

<!-- MOST POPULAR -->
<section class="most-popular">
  <h2 class="abs section-title" style="left:94px;top:1098px">Most Popular</h2>
  <div class="arrow-btn" style="left:32px;top:1276px"><svg width="10" height="10"><polyline points="6,2 3,5 6,8" fill="none" stroke="#666" stroke-width="1.2"/></svg></div>
  <div class="arrow-btn" style="left:1138px;top:1281px"><svg width="10" height="10"><polyline points="4,2 7,5 4,8" fill="none" stroke="#666" stroke-width="1.2"/></svg></div>

  <article class="product" style="left:94px;top:1161px">
    <div class="thumb" role="img" aria-label="Woman in yellow sports top and shorts" style="background:linear-gradient(180deg,#3b3b3b,#1f1f1f 60%,#c8a020 80%,#2a2a2a)"></div>
    <div class="name" style="top:285px">Finibus Bonorum<span class="stars">★★★★★</span></div>
    <div class="desc" style="top:316px">Sed ut perspiciatis unde omnis iste natus error sit voluptate...</div>
    <div class="price" style="top:362px">$122.99</div>
  </article>
  <article class="product" style="left:350px;top:1161px">
    <div class="thumb" role="img" aria-label="Flat lay of trainers, headphones, bottle and gym gear on yellow" style="background:linear-gradient(135deg,#f7c21a,#f1b80c 60%,#e2a90a)"></div>
    <div class="name" style="top:285px">Finibus Bonorum<span class="stars">★★★★★</span></div>
    <div class="desc" style="top:316px">Sed ut perspiciatis unde omnis iste natus error sit voluptate...</div>
    <div class="price" style="top:362px">$122.99</div>
  </article>
  <article class="product" style="left:608px;top:1161px">
    <div class="thumb" role="img" aria-label="Woman in black tank top and red joggers" style="background:linear-gradient(180deg,#f5f5f5,#ececec 50%,#8a1f2a 85%,#f0f0f0)"></div>
    <div class="name" style="top:285px">Finibus Bonorum<span class="stars">★★★★★</span></div>
    <div class="desc" style="top:316px">Sed ut perspiciatis unde omnis iste natus error sit voluptate...</div>
    <div class="price" style="top:362px">$122.99</div>
  </article>
  <article class="product" style="left:865px;top:1161px">
    <div class="thumb" role="img" aria-label="Woman doing a lunge with resistance bands on yellow" style="background:linear-gradient(135deg,#f4b623,#f0a818 55%,#f0515a 80%,#f4b623)"></div>
    <div class="name" style="top:285px">Finibus Bonorum<span class="stars">★★★★★</span></div>
    <div class="desc" style="top:316px">Sed ut perspiciatis unde omnis iste natus error sit voluptate...</div>
    <div class="price" style="top:362px">$122.99</div>
  </article>
</section>

<!-- WORKOUT GEAR BAND -->
<section class="workout">
  <svg class="abs" style="left:0;top:1596px" width="1200" height="441" viewBox="0 0 1200 441">
    <rect width="1200" height="441" fill="#587f96"/>
    <polygon points="220,0 838,0 873,58 258,58" fill="#fff"/>
    <polygon points="476,382 1097,382 1130,441 514,441" fill="#fff"/>
  </svg>
  <div class="abs" style="left:94px;top:1654px;width:453px;height:324px;background:#f3f3f3"></div>
  <div class="photo" role="img" aria-label="Muscular man holding a shaker bottle in a dark gym" style="left:547px;top:1654px;width:559px;height:324px;background:radial-gradient(ellipse at 50% 45%,#6b5a4c 0%,#2d2622 45%,#121010 100%)"></div>
  <div class="abs workout-tag">New Products</div>
  <div class="abs display" style="left:94px;top:1713px;width:453px;text-align:center;font-size:36px;font-weight:700;color:var(--orange);text-transform:uppercase">New</div>
  <div class="abs display" style="left:94px;top:1752px;width:453px;text-align:center;font-size:36px;color:#333;text-transform:uppercase"><b style="font-weight:700">Workout</b> Gear</div>
  <div class="abs discount-box">
    <div style="position:absolute;left:0;top:11px;width:219px;font:500 17px/1 Rajdhani,sans-serif;color:#333;text-transform:uppercase">Discount</div>
    <div style="position:absolute;left:0;top:33px;width:219px;font:500 38px/1 Rajdhani,sans-serif;color:#333">-30%</div>
  </div>
  <div class="btn" style="left:272px;top:1923px;width:98px;height:30px">Shop Now</div>
  <div class="photo" role="img" aria-label="Black tub of whey protein" style="left:456px;top:1824px;width:92px;height:158px;border-radius:12px 12px 8px 8px;background:linear-gradient(90deg,#111,#3a3a3a 40%,#0c0c0c)"></div>
</section>

<!-- NEW PRODUCTS -->
<section class="new-products">
  <h2 class="abs section-title" style="left:94px;top:2094px">New Products</h2>
  <div class="arrow-btn" style="left:32px;top:2272px"><svg width="10" height="10"><polyline points="6,2 3,5 6,8" fill="none" stroke="#666" stroke-width="1.2"/></svg></div>
  <div class="arrow-btn" style="left:1138px;top:2279px"><svg width="10" height="10"><polyline points="4,2 7,5 4,8" fill="none" stroke="#666" stroke-width="1.2"/></svg></div>

  <article class="product boxed" style="left:94px;top:2156px">
    <div class="thumb" role="img" aria-label="Protein tub with blue dumbbell weights" style="background:radial-gradient(circle at 50% 50%,#4a63a8 0%,#8d97a8 30%,#ffffff 62%)"></div>
    <div class="name" style="top:284px">Finibus Bonorum<span class="stars">★★★★★</span></div>
    <div class="desc" style="top:316px">Sed ut perspiciatis unde omnis iste natus error sit voluptate...</div>
    <div class="price" style="top:362px">$122.99</div>
  </article>
  <article class="product boxed" style="left:350px;top:2156px">
    <div class="thumb" role="img" aria-label="Green protein tub with a kettlebell" style="background:radial-gradient(circle at 45% 50%,#3fbf3a 0%,#2b2b2b 32%,#ffffff 62%)"></div>
    <div class="name" style="top:284px">Finibus Bonorum<span class="stars">★★★★★</span></div>
    <div class="desc" style="top:316px">Sed ut perspiciatis unde omnis iste natus error sit voluptate...</div>
    <div class="price" style="top:362px">$122.99</div>
  </article>
  <article class="product boxed" style="left:608px;top:2156px">
    <div class="thumb" role="img" aria-label="Pink protein tub with a pink dumbbell" style="background:radial-gradient(circle at 45% 48%,#e0457f 0%,#2b2b2b 32%,#ffffff 62%)"></div>
    <div class="name" style="top:284px">Finibus Bonorum<span class="stars">★★★★★</span></div>
    <div class="desc" style="top:316px">Sed ut perspiciatis unde omnis iste natus error sit voluptate...</div>
    <div class="price" style="top:362px">$122.99</div>
  </article>
  <article class="product boxed" style="left:865px;top:2156px">
    <div class="thumb" role="img" aria-label="Two black protein tubs with orange and red labels" style="background:linear-gradient(90deg,#fff 4%,#2a2a2a 10%,#e98a1e 35%,#2a2a2a 50%,#c8281f 70%,#2a2a2a 90%,#fff 96%)"></div>
    <div class="name" style="top:284px">Finibus Bonorum<span class="stars">★★★★★</span></div>
    <div class="desc" style="top:316px">Sed ut perspiciatis unde omnis iste natus error sit voluptate...</div>
    <div class="price" style="top:362px">$122.99</div>
  </article>
</section>

<!-- ABOUT -->
<section class="about">
  <div class="abs" style="left:0;top:2590px;width:1200px;height:382px;background:linear-gradient(90deg,#f6f6f6 0%,#f9f9f9 60%,#eef2f6 100%)"></div>
  <div class="photo" role="img" aria-label="Woman in black sportswear jogging on the spot" style="left:40px;top:2595px;width:165px;height:370px;background:linear-gradient(180deg,#f6f6f6,#2a2a2a 30%,#3a3a3a 75%,#f6f6f6)"></div>
  <h2 class="abs about-title">About <b style="font-weight:600">Our Store</b></h2>
  <div class="abs" style="left:0;width:1200px;top:2746px;text-align:center;font-size:15px;color:#333">There are many variations of passages of Lorem Ipsum available</div>
  <div class="abs" style="left:562px;top:2782px;width:76px;height:1px;background:#555"></div>
  <p class="abs" style="left:200px;width:800px;top:2796px;text-align:center;font-size:14px;line-height:23px;color:#999">Lorem ipsum dolor sit amet, consectetur adipiscing elit, sed do eiusmod tempor incididunt ut labore et dolore magna aliqua. Ut enim ad minim veniam, quis nostrud exercitation ullamco laboris nisi ut aliquip ex ea commodo consequat. Duis aute irure dolor in reprehenderit...</p>
</section>

<!-- BLOG -->
<section class="blog">
  <h2 class="abs" style="left:0;width:1200px;top:3031px;text-align:center;font:400 36px/1 Rajdhani,sans-serif;color:#333;text-transform:uppercase">Our <b style="font-weight:600">Blog</b></h2>
  <article class="post" style="left:94px;top:3097px">
    <div class="thumb" role="img" aria-label="Couple riding exercise bikes in a gym" style="background:linear-gradient(135deg,#5a4a3f,#2b2320 55%,#7a6a5e)"></div>
    <div class="date"><span>4</span><span>Mar</span></div>
    <h3>The standard Lorem Ipsum</h3>
    <div class="meta">Posted by <b>Admin</b> | <b>25 Comments</b></div>
    <p>Sed ut perspiciatis unde omnis iste error sit voluptatem accusantium doloremque laudantium...</p>
    <div class="more">→</div>
  </article>
  <article class="post" style="left:439px;top:3097px">
    <div class="thumb" role="img" aria-label="Woman stretching on the gym floor" style="background:linear-gradient(135deg,#3a3a3a,#1c1c1c 55%,#6a6a6a)"></div>
    <div class="date"><span>4</span><span>Mar</span></div>
    <h3>The standard Lorem Ipsum</h3>
    <div class="meta">Posted by <b>Admin</b> | <b>25 Comments</b></div>
    <p>Sed ut perspiciatis unde omnis iste error sit voluptatem accusantium doloremque laudantium...</p>
    <div class="more">→</div>
  </article>
  <article class="post" style="left:785px;top:3097px">
    <div class="thumb" role="img" aria-label="Woman resting on a beach after a run" style="background:linear-gradient(180deg,#e6e2dc 0%,#c9c2b6 50%,#9f9384 100%)"></div>
    <div class="date"><span>4</span><span>Mar</span></div>
    <h3>The standard Lorem Ipsum</h3>
    <div class="meta">Posted by <b>Admin</b> | <b>25 Comments</b></div>
    <p>Sed ut perspiciatis unde omnis iste error sit voluptatem accusantium doloremque laudantium...</p>
    <div class="more">→</div>
  </article>
</section>

<!-- FOOTER -->
<footer class="abs site-footer">
  <h4 class="f-head" style="left:94px">About Us</h4>
  <p class="f-text" style="left:94px;top:96px;width:200px">Sed ut perspiciatis unde omnis iste natus error sit voluptatem accusantium doloremque laudantium, totam rem aperiam eaque ipsa... <span style="color:var(--orange)">Read More</span></p>
  <div class="social"><span></span><span></span><span></span><span></span></div>

  <h4 class="f-head" style="left:333px">Quick Link</h4>
  <ul class="f-list" style="left:333px"><li>Home</li><li>About Us</li><li>Products</li><li>Blog</li><li>Contact Us</li></ul>

  <h4 class="f-head" style="left:500px">Infomation</h4>
  <ul class="f-list" style="left:500px"><li>My Account</li><li>Whishlist</li><li>Shipping Cart</li><li>Login</li><li>Sign In</li><li>Help</li></ul>

  <h4 class="f-head" style="left:665px">Contacts</h4>
  <div class="contact-row" style="top:96px"><i><svg width="12" height="12" viewBox="0 0 12 12"><path d="M6 1a3.5 3.5 0 0 0-3.5 3.5C2.5 7.5 6 11 6 11s3.5-3.5 3.5-6.5A3.5 3.5 0 0 0 6 1z" fill="#fff"/><circle cx="6" cy="4.5" r="1.2" fill="#f26b21"/></svg></i><span>218 Harbor Lane, Lorem ipsum,<br>Westfield 30452</span></div>
  <div class="contact-row" style="top:140px;align-items:center"><i><svg width="12" height="12" viewBox="0 0 12 12"><path d="M3 1.5l2 2-1 1.2c.6 1.3 1.6 2.3 2.9 2.9l1.2-1 2 2-1.2 1.6C5.500 10 2 6.500 1.500 2.700z" fill="#fff"/></svg></i><span>+1 (555) 014 2290</span></div>
  <div class="contact-row" style="top:176px;align-items:center"><i><svg width="12" height="12" viewBox="0 0 12 12"><rect x="1.5" y="3" width="9" height="6.5" fill="none" stroke="#fff" stroke-width="1.2"/><polyline points="1.5,3 6,6.5 10.5,3" fill="none" stroke="#fff" stroke-width="1.2"/></svg></i><span>hello@cobaltthreads.example</span></div>

  <h4 class="f-head" style="left:912px">Newsletter</h4>
  <p class="f-text" style="left:914px;top:98px;width:192px">We'll deliver gorgeous jewelry right to your inbox! Subscribe to our product updates:</p>
  <div class="nl-input">Enter Your Email</div>
  <div class="nl-btn">Subscribe</div>

  <div class="feature" style="left:96px"><i><svg width="26" height="20" viewBox="0 0 26 20"><rect x="1" y="4" width="14" height="10" fill="#fff"/><path d="M15 7h5l4 4v3h-9z" fill="#fff"/><circle cx="6" cy="16" r="2.4" fill="#fff" stroke="#f26b21"/><circle cx="19" cy="16" r="2.4" fill="#fff" stroke="#f26b21"/></svg></i><div><h4>Free Shipping</h4><p>Sed ut perspiciatis unde omnis iste natus error sit voluptatem</p></div></div>
  <div class="feature" style="left:472px"><i><svg width="24" height="20" viewBox="0 0 24 20"><rect x="2" y="4" width="20" height="13" rx="2" fill="none" stroke="#fff" stroke-width="1.6"/><line x1="2" y1="8" x2="22" y2="8" stroke="#fff" stroke-width="2"/></svg></i><div><h4>Secured Payment</h4><p>Sed ut perspiciatis unde omnis iste natus error sit voluptatem</p></div></div>
  <div class="feature" style="left:841px"><i><svg width="24" height="22" viewBox="0 0 24 22"><circle cx="15" cy="7" r="5" fill="none" stroke="#fff" stroke-width="1.6"/><path d="M2 15h6l3 2h6l-2 3H5z" fill="#fff"/></svg></i><div><h4>Money Back Guarantee</h4><p>Sed ut perspiciatis unde omnis iste natus error sit voluptatem</p></div></div>

  <div class="pay"><span></span><span></span><span></span><span></span></div>
  <div class="copyright">Copyright © 2019 <b>Cobalt Threads and Fuel</b>. All rights reserved.</div>
</footer>

</body>
</html>
```